Yay It's Feb already!

I am a mobile weight loss consultant. I have partnered up with the Vital Kickoff program which is based on real food. I travel to my clients at work or at home or in my own home office. My target audience is mothers -especial younger mothers with school kids and its time for my clients to focus on themselves they are worth it. I have over 10 years experience as a weight loss consultant. No contracts and no risk and i want them directed to my (social icon removed, plain square) page YayWellnessGuide or call me on 0438920574.

I am looking for a flyer to attached to his brochure early Feb for the mothers with all the kids going to back to school. ( i will attach so you can see it).
I have attached VK advertising with the girl and the banana. I do like the vk official partner somewhere on it?? I like the back drop as the girl with a banana or a mum and kids ?? I don't know

Limitied places so be quick

I have attached my logo as well.

Any questions plz ask I just need something when mothers see it, they will look twice and just chuck it in the bin??
Thank you
Maree

Just leaning how to use art huddle so I have updated my information to help you. Thank you

Reason: I am getting many great designs. I am currently on holidays and get home tomorrow and would like a couple of days to get my friends options etc before I decide. Thank you to all designers

Target Market(s)

mothers, especially young mums with kids at school- which will just be starting back at school in February.

Industry/Entity Type

Advertising

Requirements
Must have
• somehow :-
- no contracts with no risk
- experienced
- i go to them at home or work
- real food
Should not have
• The word "diet"

```html
<!DOCTYPE html>
<html lang="en">
<head>
<meta charset="utf-8">
<title>Yay It's Feb already! – Mobile Weight Loss Flyer</title>
<link href="https://fonts.googleapis.com/css2?family=Oswald:wght@600;700&family=Lato:wght@700;900&display=swap" rel="stylesheet">
<style>
  :root{
    --sky:#4b9fd5;
    --sky-deep:#3a8cc4;
    --salmon:#f08383;
    --red:#e23b3b;
    --sunny:#fcd94a;
    --ink:#1c1c1c;
    --white:#ffffff;
    --lime:#c6e05a;
    --blue-text:#1e8fd6;
    --stamp:#ee7b82;
    --leaf:#a6cc78;
    --leaf-light:#cfe3a8;
    --table:#7a5a3c;
  }
  *{margin:0;padding:0;box-sizing:border-box}
  html,body{width:1200px;height:902px;overflow:hidden;background:#f2f2f2}
  .flyer{position:relative;width:1200px;height:902px;overflow:hidden;
    background:radial-gradient(ellipse at 70% 30%,#5aaee0 0%,var(--sky) 55%,var(--sky-deep) 100%);
    font-family:"Lato",Arial,sans-serif}
  .photo{position:absolute;left:0;top:0;width:600px;height:902px;
    background:linear-gradient(180deg,var(--leaf) 0%,var(--leaf-light) 45%,#dfe6cf 70%,var(--table) 100%);
    clip-path:polygon(0 0,560px 0,548px 60px,566px 120px,546px 190px,570px 260px,550px 330px,572px 400px,548px 470px,566px 540px,544px 610px,562px 680px,540px 750px,556px 820px,546px 902px,0 902px)}
  .torn-edge{position:absolute;left:0;top:0;pointer-events:none}
  .stamp{position:absolute;left:220px;top:60px;width:210px;height:210px;border:5px solid var(--stamp);
    border-radius:50%;display:flex;align-items:center;justify-content:center;transform:rotate(-22deg)}
  .stamp::before{content:"";position:absolute;inset:12px;border:2px solid var(--stamp);border-radius:50%}
  .stamp span{font-family:"Oswald",sans-serif;font-weight:700;font-size:38px;color:var(--stamp);
    letter-spacing:1px;border-top:3px solid var(--stamp);border-bottom:3px solid var(--stamp);
    padding:0 6px;background:rgba(255,255,255,.25)}
  .real-food{position:absolute;left:335px;top:590px;width:270px;height:270px;border-radius:50%;
    border:16px solid var(--sunny);display:flex;align-items:center;justify-content:center}
  .real-food .disc{width:200px;height:200px;border-radius:50%;background:var(--white);
    display:flex;flex-direction:column;align-items:center;justify-content:center;
    font-family:"Lato",sans-serif;font-weight:900;font-size:58px;line-height:1}
  .real-food .real{color:var(--blue-text)}
  .real-food .food{color:var(--salmon)}
  .social{position:absolute;left:34px;top:792px;display:flex;align-items:center;gap:10px}
  .social .square{width:44px;height:44px;background:#3b5d9f}
  .social p{font-weight:900;font-size:19px;line-height:1.15;color:var(--ink)}
  .social p b{color:var(--red)}
  .brand{position:absolute;left:640px;top:70px;width:480px;height:130px;
    display:flex;flex-direction:column;align-items:center;justify-content:center}
  .brand .name{font-weight:900;font-size:46px;color:var(--white)}
  .brand .tag{font-weight:900;font-size:28px;color:var(--white)}
  .headline{position:absolute;left:560px;width:640px;text-align:center;font-family:"Oswald",sans-serif;
    font-weight:700;text-transform:uppercase;line-height:1;text-shadow:2px 3px 4px rgba(0,0,0,.25)}
  .h-contracts{top:232px;font-size:84px;color:var(--salmon)}
  .h-risk{top:322px;font-size:84px;color:var(--white)}
  .band{position:absolute;left:560px;top:425px;width:640px;height:125px;
    background:var(--sunny);clip-path:polygon(2% 8%,30% 0,70% 5%,100% 0,99% 100%,60% 94%,25% 100%,0 92%,3% 50%)}
  .band-text{position:absolute;left:560px;top:453px;width:640px;text-align:center;
    font-weight:900;font-size:26px;line-height:1.25;text-transform:uppercase}
  .band-text .dark{color:var(--ink)}
  .band-text .warm{color:var(--red)}
  .promise{position:absolute;left:560px;width:640px;text-align:center;text-transform:uppercase}
  .p-only{top:592px;font-family:"Oswald",sans-serif;font-weight:700;font-size:38px;color:var(--lime)}
  .p-only em{font-style:normal;color:var(--salmon)}
  .p-want{top:636px;font-family:"Oswald",sans-serif;font-weight:700;font-size:68px;color:var(--white);
    text-shadow:2px 3px 4px rgba(0,0,0,.25)}
  .p-limit{top:752px;font-weight:900;font-size:28px;color:var(--white)}
  .p-limit em{font-style:normal;color:var(--lime)}
  .call-band{position:absolute;left:560px;top:815px;width:640px;height:87px;background:var(--sunny);
    clip-path:polygon(3% 10%,40% 0,100% 6%,100% 100%,0 100%,1% 40%)}
  .call{position:absolute;left:560px;top:838px;width:640px;text-align:center;font-weight:900;font-size:35px;text-transform:uppercase}
  .call .who{color:var(--red)}
  .call .num{color:var(--blue-text)}
</style>
</head>
<body>
<main class="flyer">
  <div class="photo" role="img" aria-label="Photo: milk poured from a jug into a glass on a wooden table, green garden behind"></div>
  <svg class="torn-edge" width="600" height="902" viewBox="0 0 600 902" aria-hidden="true">
    <polyline fill="none" stroke="#ffffff" stroke-width="9" points="560,0 548,60 566,120 546,190 570,260 550,330 572,400 548,470 566,540 544,610 562,680 540,750 556,820 546,902"/>
  </svg>

  <div class="stamp"><span>EXPERIENCED</span></div>

  <div class="real-food"><div class="disc"><span class="real">REAL</span><span class="food">FOOD</span></div></div>

  <div class="social">
    <div class="square"></div>
    <p>Like Us<br><b>YayWellnessGuide</b></p>
  </div>

  <div class="brand">
    <span class="name">YayWellnessGuide</span>
    <span class="tag">Lifestyle Coach</span>
  </div>

  <h1 class="headline h-contracts">No Contracts</h1>
  <h2 class="headline h-risk">With No Risk</h2>

  <div class="band"></div>
  <p class="band-text">
    <span class="dark">Mobile weight loss consultant- offering</span><br>
    <span class="warm">Consultations at your home or work</span>
  </p>

  <p class="promise p-only">You will only <em>lose the weight</em></p>
  <p class="promise p-want">You want to lose</p>
  <p class="promise p-limit">Limited appointments <em>so be quick</em></p>

  <div class="call-band"></div>
  <p class="call"><span class="who">Call Maree</span> <span class="num">0438 920 574</span></p>
</main>
</body>
</html>
```